wine label design

i'm a fine wine store based in new zealand which buys quality bulk wine and bottles it, passing on the significant savings onto the customer. i require a brand name and design which is cool/ sharp and contempory. the wines will be all still wines, there won't be any sparkling wines under this brand. i've used brand names like harbourlight wine company for previous designs/label but want something more edgier. we thought about a brand name 'fair and square' or 'harbourlight wine co' but couldn't get a design to match the title of brand, if you have any thoughts on this send thru your design. take into account color they have to be bold as i am printing these thru a digital printer. the label is a wrap around design, the dimensions are approximately 80 or 90 mm high and 210 mm wide. have a look at these links, i think they have some x-factor to them: http://www.merivaleshop.com/store/product_images/p/855/lumen__34476_zoom.jpg: OR

http://static3.cellarfinder.net/images/labels/35/24/quiet-harbour-shiraz-petite-sirah-south-australia-10203524.jpg: OR

http://www.orchardvane.com/ui/productimages/25223/25223_w240.jpg: OR

http://www.bellvinos.co.nz/images/viewWinery.php?pic=238291

Take into account i have to be able put a wine desription on the back label, barcode and a few technical details required by law. on the front label all i require is space to put the grape variety, area and vintage. i need the grape type to really stand out.
Updates

Reason: hi, the designs coming thru look good, just need a little more changes, also please read thru the brief, there are a few things i have noted such as label size etc etc

Target Market(s)

am after a label the cool/edgy/contempoary that appeals to the educated well off customer that willing to give something new a go by the look of the label that is cool and edgy.

Industry/Entity Type

Boutique

Requirements
Must have
• bold bold bold, it must stand out on the shelf
Nice to have
• a title/brand name that links what i'm doing, from what i'm doing the name 'harbourlight wine co' is probably best suited.
Should not have
• basic boring artwork and small text, the bigger the text the better

```html
<!DOCTYPE html>
<html lang="en">
<head>
<meta charset="utf-8">
<title>Tavro – Merlot Cabarnet label</title>
<link rel="stylesheet" href="https://fonts.googleapis.com/css2?family=Passion+One:wght@700&family=PT+Sans:wght@400;700&display=swap">
<style>
  :root {
    --backdrop: #c4105e;
    --label: #2b2b2d;
    --band: #1c1c1e;
    --disc: #141415;
    --ring-rim: #2e2e30;
    --magenta: #e8125f;
    --yellow: #f4ee1a;
    --orange: #f59a1c;
    --star: #4a4a4d;
    --muted: #6a6a6e;
  }
  * { margin: 0; padding: 0; box-sizing: border-box; }
  html, body { width: 1200px; height: 900px; overflow: hidden; }
  body {
    background: var(--backdrop);
    font-family: "PT Sans", sans-serif;
    position: relative;
  }
  .label {
    position: absolute;
    left: 150px; top: 50px;
    width: 900px; height: 800px;
    background: var(--label);
    overflow: hidden;
  }
  .label-band {
    position: absolute;
    left: 365px; top: 0;
    width: 170px; height: 100%;
    background: var(--band);
  }
  .seal-ring {
    position: absolute;
    left: 175px; top: 125px;
    width: 550px; height: 550px;
  }
  .seal-disc {
    position: absolute;
    left: 225px; top: 175px;
    width: 450px; height: 450px;
    border-radius: 50%;
    background: var(--disc);
    box-shadow: 0 0 0 8px var(--ring-rim);
    text-align: center;
  }
  .vintage {
    position: absolute;
    top: 98px; width: 100%;
    font-size: 24px;
    letter-spacing: 1px;
    color: var(--magenta);
  }
  .brand-name {
    position: absolute;
    top: 140px; width: 100%;
    font-family: "Passion One", sans-serif;
    font-weight: 700;
    font-size: 132px;
    line-height: 1;
    letter-spacing: -2px;
    color: var(--magenta);
  }
  .rating {
    position: absolute;
    top: 272px; left: 50%;
    transform: translateX(-50%);
    width: 190px; height: 56px;
  }
  .variety {
    position: absolute;
    top: 336px; width: 100%;
    font-size: 36px;
    letter-spacing: 0.5px;
    color: var(--magenta);
  }
  .brand-dot {
    position: absolute;
    left: 200px; top: 390px;
    width: 50px; height: 50px;
    border-radius: 50%;
    background: var(--star);
  }
  .region {
    position: absolute;
    left: 365px; top: 705px;
    width: 170px;
    text-align: center;
    font-weight: 700;
    font-size: 30px;
    line-height: 1.05;
    color: var(--muted);
  }
</style>
</head>
<body>
  <main class="label">
    <div class="label-band"></div>

    <svg class="seal-ring" viewBox="0 0 550 550" role="img" aria-label="Ring of yellow, orange and red diamond pattern around the seal">
      <defs>
        <linearGradient id="ring-tones" x1="0" y1="0" x2="1" y2="1">
          <stop offset="0" stop-color="#f4ee1a"/>
          <stop offset="0.5" stop-color="#f59a1c"/>
          <stop offset="1" stop-color="#e8125f"/>
        </linearGradient>
      </defs>
      <path fill="url(#ring-tones)" fill-rule="evenodd"
        d="M275 0 A275 275 0 1 1 274.9 0 Z M275 42 A233 233 0 1 0 275.1 42 Z"/>
    </svg>

    <section class="seal-disc">
      <p class="vintage">2010</p>
      <h1 class="brand-name">TAVRO.</h1>
      <svg class="rating" viewBox="0 0 190 56" aria-label="Three stars">
        <g fill="var(--star)">
          <polygon points="30,2 37,20 56,21 41,33 46,52 30,41 14,52 19,33 4,21 23,20"/>
          <polygon points="95,2 102,20 121,21 106,33 111,52 95,41 79,52 84,33 69,21 88,20"/>
          <polygon points="160,2 167,20 186,21 171,33 176,52 160,41 144,52 149,33 134,21 153,20"/>
        </g>
      </svg>
      <p class="variety">MERLOT CABARNET</p>
      <span class="brand-dot"></span>
    </section>

    <p class="region">NEW<br>ZEALAND</p>
  </main>
</body>
</html>
```